Wine labels Velmora Wine Council - Nueva etiqueta El Consejo Regulador de vinos de Albarrán

Velmora Wines Council, based in southern Spain, are looking to create a new suite of wine labels which retain the elegance of the Velmora Wines industry while reinvigorating their image to the modern era and a new generation of Sherry Wine lovers. These labels will be used across the Velmora Wines Council's range of wines for the promotion of the Velmora Wines industry.

Your design must present at least two styles of Velmora Wines which demonstrate an elegant, modern interpretation and understanding of the unique mood and personality for these wines and the essence of southern Spain.

10 labels will be created based on the winning design, one for each of the unique varieties of Velmora Wines within the collection. This collection comprises of several different wine varieties including: Fino, Manzanilla, Amontillado, Oloroso, Palo Cortado, Medium, Cream, Pale Cream, Pedro Ximenez and Moscatel.

We recommend you visit our website www.velmora-vinos.example/wines as the source to understanding the origins and unique personality of these diverse wines.

El Consejo Regulador de los Vinos de Albarrán y Tordesal quiere renovar las etiquetas de los vinos utilizados para sus actividades de promoción genérica. Esta colección de vinos comprende las tipologías más importantes de la región que incluye: fino, manzanilla, amontillado, oloroso, palo cortado, pale cream, medium, cream, pedro ximénez y moscatel. Por lo tanto se precisan 10 etiquetas, una para cada uno de los vinos mencionados.
Updates

Project Deadline Extended
Reason: Due to some confusion with the deadline we wish to officially extend the deadline to allow designers one last week to submit their entries.

Target Market(s)

Industry, journalists, media, sommeliers, chefs, wine writers

Industry/Entity Type

Council

Requirements
Must have
• Front and Back label plus capsule:
• Front label can have either of the two official logos of the Velmora Wine council titled Vinos de Albarrán Digital or not, this is optional. Must include: Vino selecionado por el Consejo Regulador de la Denominacion de Origen, Name of the variety of wine eg FINO, percentage of alcohol eg 15% and quantity 75 cl.
• The back of the label must include the council logo titled Sellora and 4 additional logos positioned smaller. The Europa logo must appear larger than the 3 other logos. Space for descriptive text about the wine is also required.
• The dimensions of the bottle can be found at this link http://www.vidrialto.example/es/catalogo/vinos-y-espumosos/bordelesas/bd-orla
• Altura:305 mm
• Diámetro base:76,20 mm
• Diámetro hombro:82 mm
• Tipo boca:Cetie
• Peso:750 gr
• Capacidad:75 cl
• Etiqueta delantera y trasera y capsula
• La etiqueta delantera puede incluir el logo oficial del Consejo Regulador o el logo digital, o ninguno, esto es opcional. Debe incluir el siguiete texto: Vino selecionado por el Consejo Regulador de la Denominacion de Origen, el nombre de la variedad del vino, por ejemplo Fino, el porcentaje de alcohol, por ejemplo 15%, y la capacidad 75cl.
• La etiqueta trasera debe incluir el logo oficial Sellora del Consejo, y cuatro logos adicionales con una dimension menor. El Logo de ¨Europa invierte en las zonas rurales¨ debe ser de mayor tamaño que los otros. Se precisa espacio para el texto descriptivo de los vinos.
• Las dimensiones de la botella se puede encontrar en este enlace
• http://www.vidrialto.example/es/catalogo/vinos-y-espumosos/bordelesas/bd-orla
• Altura:305 mm
• Diámetro base:76,20 mm
• Diámetro hombro:82 mm
• Tipo boca:Cetie
• Peso:750 gr
• Capacidad:75 cl
Nice to have
• See our website velmora-vinos.example to understand the origin of the wines. Ver nuestra página web velmora-vinos.example para mejor entender los vinos.
Should not have
• Images of catavinos or stereotypical images from Spain such as flamenco dancers or guitars.

```html
<!DOCTYPE html>
<html lang="es">
<head>
<meta charset="utf-8">
<title>Velmora Wine Council – Fino labels</title>
<link href="https://fonts.googleapis.com/css2?family=Marcellus&family=Pinyon+Script&family=Roboto+Condensed:wght@300&display=swap" rel="stylesheet">
<style>
  :root{
    --backdrop:#6f6f6f;
    --plum:#6b3a5a;
    --plum-deep:#4a1d3a;
    --cream:#e4e1d3;
    --ivory:#ede9e3;
    --gold:#c8995a;
    --gold-text:#d6a85a;
    --magenta:#9b2a7a;
    --night:#1f1815;
    --ink:#6a625c;
    --serif:"Marcellus", "Times New Roman", serif;
    --script:"Pinyon Script", cursive;
    --sans:"Roboto Condensed", Arial, sans-serif;
  }
  *{box-sizing:border-box;margin:0;padding:0}
  html,body{width:1200px;height:1080px;overflow:hidden;background:var(--backdrop)}
  .canvas{position:relative;width:1200px;height:1080px;display:flex;justify-content:center;align-items:center;gap:60px}
  .label{position:relative;width:330px;height:622px;overflow:hidden}
  .label > *{position:absolute}
  .brand{left:0;right:0;text-align:center;font-family:var(--serif);line-height:1}
  .brand-dot{display:block;width:12px;height:12px;border-radius:50%;margin:0 auto 8px;border:1.5px solid currentColor}
  .brand-name{font-size:12px;letter-spacing:.5px;text-transform:uppercase;white-space:nowrap}
  .brand-sub{font-size:6px;letter-spacing:2px;margin-top:3px;text-transform:uppercase;white-space:nowrap}
  .variety{left:0;right:0;text-align:center;font-family:var(--serif);line-height:1}
  .variety .dash{display:inline-block;width:30px;height:2px;background:currentColor;vertical-align:middle;margin-right:-4px;position:relative;top:-6px}
  .art{left:50%;transform:translateX(-50%)}
  .badge{width:72px;height:36px;background:#fff;right:8px}
  .badge::before,.badge::after{content:"";position:absolute;background:#9aa39a;top:8px;height:20px}
  .badge::before{left:8px;width:12px}
  .badge::after{left:28px;width:34px;height:10px;top:13px;background:#6a9a3a}
  .spec{font-family:var(--sans);font-weight:300;font-size:16px;bottom:12px}
  .spec.alc{left:6px}
  .spec.vol{right:8px}

  /* Label one: plum and cream */
  .label--plum{background:var(--cream)}
  .label--plum .top-band{left:0;top:0;width:100%;height:99px;background:var(--plum)}
  .label--plum .brand{top:22px;color:#d9b9b5}
  .label--plum .foot-band{left:0;bottom:0;width:100%;height:80px;background:var(--plum-deep)}
  .label--plum .variety-kind{top:148px;font-size:34px;color:var(--ink)}
  .label--plum .variety-name{top:182px;font-size:68px;color:var(--ink)}
  .label--plum .art{top:262px;width:240px;height:300px;border-radius:48% 48% 30% 30%;background:radial-gradient(circle at 50% 40%,#7a2a6a 0%,#5a1a4a 55%,#8ea043 75%,transparent 78%)}
  .label--plum .badge{bottom:20px}

  /* Label two: ivory and gold */
  .label--ivory{background:var(--ivory)}
  .label--ivory .stripe-top{left:152px;top:0;width:26px;height:36px;background:var(--gold)}
  .label--ivory .stripe-low{left:152px;top:245px;width:26px;bottom:0;background:var(--gold)}
  .label--ivory .brand{top:20px;color:var(--ink)}
  .label--ivory .brand .brand-name{margin-top:6px}
  .label--ivory .variety-kind{top:105px;font-family:var(--script);font-size:50px;color:var(--ink)}
  .label--ivory .variety-name{top:170px;font-size:66px;color:var(--ink)}
  .label--ivory .rule{left:95px;top:242px;width:145px;height:1px;background:var(--ink)}
  .label--ivory .art{top:270px;width:200px;height:290px;border-radius:50% 50% 40% 40%;background:radial-gradient(circle at 50% 38%,#8a2f6e 0%,#6a2050 45%,rgba(106,32,80,.35) 70%,transparent 74%)}
  .label--ivory .badge{bottom:50px}
  .label--ivory .spec{color:var(--ink)}

  /* Label three: night and magenta */
  .label--night{background:var(--night)}
  .label--night .stripe{left:152px;top:0;width:26px;bottom:0;background:var(--magenta)}
  .label--night .brand-block{left:118px;top:12px;width:94px;height:84px;background:var(--gold)}
  .label--night .brand{left:118px;right:auto;width:94px;top:28px;color:#7a5a3a}
  .label--night .brand .brand-name{font-size:7px;letter-spacing:0}
  .label--night .brand .brand-sub{font-size:4.5px;letter-spacing:1px}
  .label--night .band{left:0;top:165px;width:100%;height:79px;background:var(--magenta);border-top:2px solid var(--gold-text);border-bottom:2px solid var(--gold-text)}
  .label--night .variety-name{top:172px;font-size:66px;color:var(--gold-text)}
  .label--night .variety-kind{top:255px;font-size:30px;color:var(--gold-text);letter-spacing:1px}
  .label--night .art{top:290px;width:230px;height:215px;border-radius:50%;background:radial-gradient(circle at 50% 45%,#a03083 0%,#7a1f62 45%,rgba(122,31,98,.3) 70%,transparent 74%)}
  .label--night .seal-text{left:0;right:0;top:490px;text-align:center;font-family:var(--serif);font-size:12px;line-height:1.15;color:var(--gold-text);text-transform:uppercase}
  .label--night .badge{bottom:38px}
  .label--night .spec{color:#cfc7bd}
</style>
</head>
<body>
<main class="canvas">

  <section class="label label--plum" aria-label="Etiqueta Sherry Fino, versión ciruela">
    <div class="top-band"></div>
    <div class="brand"><span class="brand-dot"></span><div class="brand-name">Vinos de Albarrán</div><div class="brand-sub">Velmora Wines</div></div>
    <div class="variety variety-kind">SHERRY</div>
    <div class="variety variety-name"><span class="dash"></span>FINO</div>
    <div class="foot-band"></div>
    <div class="art" role="img" aria-label="Ilustración de racimo de uvas moradas con hojas de vid verdes y raíces"></div>
    <div class="badge" aria-hidden="true"></div>
  </section>

  <section class="label label--ivory" aria-label="Etiqueta Sherry Fino, versión marfil y oro">
    <div class="stripe-top"></div>
    <div class="stripe-low"></div>
    <div class="brand"><span class="brand-dot"></span><div class="brand-name">Vinos de Albarrán</div><div class="brand-sub">Velmora Wines</div></div>
    <div class="variety variety-kind">Sherry</div>
    <div class="variety variety-name"><span class="dash"></span>FINO</div>
    <div class="rule"></div>
    <div class="art" role="img" aria-label="Ilustración de racimo de uvas granate con hojas de vid"></div>
    <div class="badge" aria-hidden="true"></div>
    <div class="spec alc">ALC. 15%</div>
    <div class="spec vol">75 CL</div>
  </section>

  <section class="label label--night" aria-label="Etiqueta Fino Sherry, versión noche y magenta">
    <div class="stripe"></div>
    <div class="brand-block"></div>
    <div class="brand"><span class="brand-dot"></span><div class="brand-name">Vinos de Albarrán</div><div class="brand-sub">Velmora Wines</div></div>
    <div class="band"></div>
    <div class="variety variety-name"><span class="dash"></span>FINO</div>
    <div class="variety variety-kind">SHERRY</div>
    <div class="art" role="img" aria-label="Ilustración de racimo de uvas magenta y doradas con hojas de vid"></div>
    <p class="seal-text">Vino seleccionado<br>por el Consejo Regulador<br>de la Denominación de Origen</p>
    <div class="badge" aria-hidden="true"></div>
    <div class="spec alc">ALC. 15%</div>
    <div class="spec vol">75 CL</div>
  </section>

</main>
</body>
</html>
```